Flyer Design Project

opening a preschool and need to hand out flyers to advertise at an expo on Feb.1st. It is geared toward 3-4 year old potty trained children. I have more that 10+ years teaching experience and it will be a private preschool with small class sizes and individual instruction and attention. You can look at the website, it is www.sunnyacornplayhouse.net. I tried to make a flyer but I can't make it with high enough resolution. I attached the logo and my attempted flyer.

Preschool

```html
<!DOCTYPE html>
<html lang="en">
<head>
<meta charset="utf-8">
<title>Sunny Acorn Playhouse – Preschool Flyer</title>
<link rel="stylesheet" href="https://fonts.googleapis.com/css2?family=Archivo+Narrow:wght@700&family=Chewy&family=Open+Sans:wght@400;600&family=Tinos:ital,wght@1,700&display=swap">
<style>
  :root {
    --sky-deep: #a9d3ef;
    --sky-light: #f4f9fd;
    --band-blue: #4a8fd0;
    --grass-dark: #3f8a1e;
    --grass-light: #8cc63f;
    --navy: #2b3190;
    --ink: #1a1a1a;
    --white: #ffffff;
    --panel: rgba(255, 255, 255, 0.42);
    --green: #8cc63f;
    --magenta: #ec1c8c;
    --yellow: #f2ec1c;
    --red: #e8232a;
    --badge-pink: #ec1c8c;
    --badge-rim: #f7ea1a;
    --button: #f6e21a;
    --button-ink: #2a2a2a;
    --display: "Chewy", "Arial Rounded MT Bold", "Arial Black", sans-serif;
    --italic: "Tinos", "Times New Roman", serif;
  }
  * { margin: 0; padding: 0; box-sizing: border-box; }
  html, body { width: 1200px; height: 780px; overflow: hidden; background: var(--white); }
  .flyer {
    position: relative; width: 1200px; height: 780px; overflow: hidden;
    background: radial-gradient(ellipse at 38% 30%, var(--sky-light) 0%, #dcebf7 40%, var(--sky-deep) 100%);
    font-family: "Open Sans", sans-serif;
  }
  .scenery { position: absolute; inset: 0; }
  .panel-left {
    position: absolute; left: 30px; top: 15px; width: 550px; height: 748px;
    background: var(--panel);
  }
  .brand { position: absolute; text-align: center; color: var(--navy); }
  .brand-name {
    display: flex; align-items: center; justify-content: center; gap: 10px;
    font-weight: 600; color: var(--navy); letter-spacing: 0.5px;
  }
  .brand-dot { width: 22px; height: 22px; border-radius: 50%; background: var(--navy); flex: none; }
  .brand-tagline { color: var(--ink); font-weight: 400; white-space: nowrap; }
  .brand--left { left: 195px; top: 332px; width: 220px; }
  .brand--left .brand-name { font-size: 21px; line-height: 1.1; }
  .brand--left .brand-tagline { font-size: 11px; margin-top: 14px; }
  .brand--top { left: 895px; top: 70px; width: 260px; }
  .brand--top .brand-name { font-size: 25px; line-height: 1.1; }
  .brand--top .brand-tagline { font-size: 13px; margin-top: 22px; }
  .contact { position: absolute; left: 110px; top: 530px; width: 380px; text-align: center; color: var(--white); font-style: normal; }
  .contact-title { font-family: var(--display); font-size: 46px; letter-spacing: 1px; line-height: 1; }
  .contact-line { font-family: var(--italic); font-style: italic; font-weight: 700; font-size: 20px; line-height: 1.35; margin-top: 12px; }
  .contact-email { font-family: var(--italic); font-style: italic; font-weight: 700; font-size: 18px; margin-top: 18px; }
  .contact-phone { font-family: var(--display); font-size: 28px; letter-spacing: 1px; margin-top: 12px; }
  .headline {
    position: absolute; left: 718px; top: 208px; width: 400px;
    transform: rotate(-9deg); transform-origin: left top;
    font-family: var(--display); font-weight: 400; line-height: 0.82;
  }
  .headline > span { display: block; }
  .headline .lead { font-family: var(--italic); font-style: italic; font-weight: 700; font-size: 19px; color: var(--ink); margin-left: 20px; line-height: 1.2; }
  .headline .big {
    font-size: 86px; white-space: nowrap;
    text-shadow: 3px 0 0 var(--white), -3px 0 0 var(--white), 0 3px 0 var(--white), 0 -3px 0 var(--white),
                 2px 2px 0 var(--white), -2px -2px 0 var(--white), 2px -2px 0 var(--white), -2px 2px 0 var(--white),
                 4px 5px 6px rgba(0,0,0,0.35);
  }
  .c-green { color: var(--green); } .c-magenta { color: var(--magenta); }
  .c-yellow { color: var(--yellow); } .c-red { color: var(--red); } .c-ink { color: var(--ink); }
  .line-two { margin-left: -6px; }
  .line-three { margin-left: 6px; }
  .headline .tail { font-family: var(--italic); font-style: italic; font-weight: 700; font-size: 18px; color: var(--ink); text-align: right; margin-right: 36px; margin-top: -6px; line-height: 1.2; }
  .early-bird {
    position: absolute; left: 623px; top: 530px; width: 150px; height: 118px;
    background: var(--badge-pink); border: 6px solid var(--badge-rim); border-radius: 16px;
    transform: rotate(-12deg); box-shadow: 3px 4px 6px rgba(0,0,0,0.3);
    display: flex; align-items: center; justify-content: center; text-align: center;
    font-family: var(--display); font-size: 27px; line-height: 1; color: var(--white);
    text-shadow: 1px 1px 0 #5a0d35, -1px -1px 0 #5a0d35, 1px -1px 0 #5a0d35, -1px 1px 0 #5a0d35;
  }
  .offer {
    position: absolute; left: 800px; top: 576px; width: 340px; text-align: center;
    font-family: var(--italic); font-style: italic; font-weight: 700; font-size: 18px; line-height: 1.3; color: var(--white);
    text-shadow: 0 1px 3px rgba(0,0,0,0.35);
  }
  .enrol-button {
    position: absolute; left: 790px; top: 678px; width: 244px; height: 36px;
    background: var(--button); border-radius: 18px;
    display: flex; align-items: center; gap: 8px; padding-left: 7px;
    font-family: "Archivo Narrow", "Arial Narrow", sans-serif; font-weight: 700; font-size: 20px; color: var(--button-ink);
  }
  .enrol-arrow { width: 24px; height: 24px; flex: none; }
</style>
</head>
<body>
<main class="flyer">
  <svg class="scenery" width="1200" height="780" viewBox="0 0 1200 780" role="img" aria-label="Bright sky with sun rays above a rolling green grass hill">
    <defs>
      <linearGradient id="grass" x1="0" y1="0" x2="0" y2="1">
        <stop offset="0" stop-color="#8cc63f"/>
        <stop offset="1" stop-color="#3f8a1e"/>
      </linearGradient>
    </defs>
    <path d="M0 580 C 250 480, 500 455, 700 458 C 900 462, 1080 510, 1200 550 L1200 780 L0 780 Z" fill="url(#grass)"/>
    <polygon points="588,0 1200,0 1200,8 588,102" fill="#4a8fd0"/>
  </svg>

  <section class="panel-left" aria-hidden="true"></section>

  <div class="brand brand--left">
    <div class="brand-name"><span class="brand-dot"></span><span>Sunny Acorn<br>Playhouse</span></div>
    <div class="brand-tagline">Little Steps Toward Big Dreams</div>
  </div>

  <address class="contact">
    <div class="contact-title">Contact Us</div>
    <div class="contact-line">4120 Maple Crest Lane Lindenvale,<br>CO 80455</div>
    <div class="contact-email">hello@sunnyacornplayhouse.net</div>
    <div class="contact-phone">720-555-0148</div>
  </address>

  <div class="brand brand--top">
    <div class="brand-name"><span class="brand-dot"></span><span>Sunny Acorn<br>Playhouse</span></div>
    <div class="brand-tagline">Little Steps Toward Big Dreams</div>
  </div>

  <h1 class="headline">
    <span class="lead">we give your child</span>
    <span class="big"><span class="c-green">a </span><span class="c-magenta">safe</span></span>
    <span class="big line-two"><span class="c-yellow">happy </span><span class="c-ink">&amp;</span></span>
    <span class="big line-three c-red">fun-filled</span>
    <span class="tail">education</span>
  </h1>

  <div class="early-bird">Early<br>Bird<br>Special!</div>

  <p class="offer">Enrol before<br>1st February 2016 and get<br>your APPLICATION FEE WEIVER</p>

  <div class="enrol-button">
    <svg class="enrol-arrow" viewBox="0 0 24 24" aria-hidden="true">
      <circle cx="12" cy="12" r="11" fill="#2a2a2a"/>
      <path d="M9.5 6.5 L15 12 L9.5 17.5" fill="none" stroke="#f6e21a" stroke-width="3" stroke-linecap="round" stroke-linejoin="round"/>
    </svg>
    <span>ENROLMENT ONGOING</span>
  </div>
</main>
</body>
</html>
```